Travel Company Itinerary and Travel Packet

I run a travel company (agency) that organizes trips (any length i.e. day, week, month, or longer) to countries (Israel, Italy, Greece, etc). Regardless of the destination, we want to provide appealing, professional, and clean materials. We are a firm believer that our product is not just the trip but in everything we do...from our communication to our written/printed materials and online presence. Today we are specifically looking for a template that we can use to share one's trip/itinerary. Ideally what you would create would be a template we could populate with specific information for the client about the day-to-day of their trip, who we are, the hotels they are staying in, the highlights, what to pack, and where to eat, etc. To be more specific, this template should consist of the following:
1. Title Page (including contact info...however this could go where you see fit)
2. About Us (blurb about us at the company),
3. A highlights page of the trip and services included - this could be used as standalone marketing material for our clients to promote trips. (look at the Italy example)
4. A timeline of the process
5. A summary of the trip, bullet point/all one 1 page
6. A day-by-day itinerary page of what they are doing, and where they are staying (each day on its own page - should be the same template repeated for each day.
7. Recommended Hotels to choose from
8. Recommended Restaurants to eat at
9. A pricing page (per person, per group, itemized down to each experience.
10. A packing List
11. A letterhead that could be used for a cover letter
12. Each page should use pictures...a template where one could insert photos per page based on where the trip is going as well as stock imaging that brings the document to life for the reader. (see examples in uploaded files).

We've attached a few that we've seen in the industry that appeals to us and our tastes, but the template we are looking for is even more eye-popping, user-friendly, and communicates a high level of service just by seeing the document. It communicates our brand. Each attached example has elements we like and don't like and will give you. a good picture (we hope), but you'll notice the list we gave you provides a more robust end product...in other words we want more than these examples as we see great potential in including each layer of information with the ability to pick and choose what to include (from all of it to just the highlights page).

Link to Brand Assets- https://files.plovanexa.net/share/folders/8Kd24mTqZrw91XbLcVn3pYe60hJ?mode=view
Updates

We need a few days to review the designs and had a few requests for an extension if possible. I've also uploaded sample itineraries for Israel as requested by a few designers. Much appreciated

Target Market(s)

Any client of ours traveling - school, groups, families, big spenders etc

Industry/Entity Type

Travel Industry

Requirements
Must have
• See above list - if clarification is needed, I'm happy to give.

```html
<!DOCTYPE html>
<html lang="en">
<head>
<meta charset="utf-8">
<title>Velora – Italy Travel Packet</title>
<link href="https://fonts.googleapis.com/css2?family=Questrial&family=Arimo:wght@400;700&display=swap" rel="stylesheet">
<style>
  :root{
    --cream:#fbf3ea;
    --navy:#1b2b42;
    --orange:#f26b21;
    --orange-light:#f7942f;
    --copper:#c8702b;
    --ink:#2b2b2b;
    --body:#3a3a3a;
    --muted:#666;
    --green:#4a9d2f;
  }
  *{margin:0;padding:0;box-sizing:border-box}
  html,body{width:1200px;height:594px;overflow:hidden;background:var(--cream)}
  body{position:relative;font-family:"Arimo",Arial,sans-serif;color:var(--body)}
  .page{position:absolute;top:48px;width:354px;height:500px;background:#fff;box-shadow:0 0 3px rgba(0,0,0,.18);overflow:hidden}
  .page--hotels{left:40px}
  .page--offer{left:420px}
  .page--packing{left:803px}
  .page__header{position:absolute;left:0;top:0;width:354px;height:290px;display:block}
  .brand{position:absolute;left:12px;top:18px;display:flex;align-items:center;gap:6px;font-family:"Questrial",sans-serif;font-size:25px;color:var(--navy);letter-spacing:.5px}
  .brand__dot{width:16px;height:16px;border-radius:50%;background:var(--orange)}
  .page__footer{position:absolute;left:0;bottom:0;width:100%;background:var(--navy)}
  .page--hotels .page__footer{height:9px}
  .page--packing .page__footer{height:4px}

  /* hotel columns */
  .hotel{position:absolute;top:302px;width:150px}
  .hotel--sorrento{left:10px}
  .hotel--roma{left:189px}
  .hotel__stay{font-family:"Questrial",sans-serif;font-size:9px;font-weight:400;color:var(--ink);letter-spacing:.2px}
  .hotel__name{font-family:"Questrial",sans-serif;font-size:13.5px;font-weight:400;color:var(--orange);margin-top:3px;letter-spacing:.3px;white-space:nowrap}
  .hotel__room{font-family:"Questrial",sans-serif;font-size:7.2px;color:var(--ink);margin-top:7px}
  .hotel__text{font-size:5.3px;line-height:9.5px;text-align:justify;margin-top:11px;color:var(--body)}
  .hotel__text p+p{margin-top:9.5px}
  .hotel__link{font-family:"Questrial",sans-serif;font-size:7.2px;color:var(--orange);margin-top:8px}

  /* offer page */
  .promise{position:absolute;left:33px;top:234px;display:flex;gap:12px;align-items:center}
  .promise__badge{width:47px;height:47px;flex:none}
  .promise__list{font-family:"Questrial",sans-serif;font-size:6.4px;line-height:9px;color:var(--ink);width:232px}
  .promise__list p{margin-bottom:3px}
  .price{position:absolute;top:296px;height:51px;display:flex;flex-direction:column;align-items:center;justify-content:center;color:#fff;font-family:"Questrial",sans-serif}
  .price--person{left:5px;width:172px;background:var(--copper)}
  .price--couple{left:177px;width:172px;background:var(--navy)}
  .price__label{font-size:9px;letter-spacing:.3px}
  .price__value{font-size:12.5px;margin-top:3px;letter-spacing:.3px}
  .terms{position:absolute;top:360px;width:162px}
  .terms--conditions{left:5px}
  .terms--cancel{left:186px}
  .terms__title{font-family:"Questrial",sans-serif;font-size:8.4px;font-weight:400;color:var(--navy)}
  .terms__rule{width:12px;height:1px;background:var(--orange);margin:4px 0 6px}
  .terms__text{font-size:4.6px;line-height:8.8px;color:var(--muted);text-align:justify}
  .terms--cancel .terms__text p{line-height:6px;margin-bottom:6px;text-align:left}
  .terms__text strong{color:var(--orange);font-weight:700}
  .page--offer .page__footer{height:31px;display:flex;flex-direction:column;align-items:center;justify-content:center;font-family:"Questrial",sans-serif;font-size:6.4px;color:#fff;line-height:9.5px;letter-spacing:.2px}
  .page__footer em{font-style:normal;color:var(--orange)}

  /* packing page */
  .pack{position:absolute;width:105px}
  .pack__title{font-family:"Questrial",sans-serif;font-size:7.4px;font-weight:400;color:var(--navy);letter-spacing:.2px;margin-bottom:8px}
  .pack__list{list-style:none}
  .pack__item{font-size:5.4px;height:11.9px;display:flex;align-items:center;gap:6px;color:var(--body)}
  .pack__item::before{content:"";width:4px;height:4px;border:0.6px solid #444;flex:none}
</style>
</head>
<body>

<!-- Hotels page -->
<section class="page page--hotels">
  <svg class="page__header" viewBox="0 0 354 290">
    <defs>
      <linearGradient id="romeDusk" x1="0" y1="0" x2="0" y2="1">
        <stop offset="0" stop-color="#e8a062"/>
        <stop offset=".35" stop-color="#b8735a"/>
        <stop offset=".7" stop-color="#4b4f73"/>
        <stop offset="1" stop-color="#2d3558"/>
      </linearGradient>
      <linearGradient id="bandA" x1="0" y1="0" x2="1" y2="0">
        <stop offset="0" stop-color="var(--orange-light)"/><stop offset=".5" stop-color="var(--orange)"/><stop offset="1" stop-color="var(--orange-light)"/>
      </linearGradient>
    </defs>
    <rect role="img" aria-label="Photo: Rome square with fountain and grand steps at dusk" width="354" height="290" fill="url(#romeDusk)"/>
    <path d="M0 0H190C150 22 95 66 0 76Z" fill="#fff"/>
    <path d="M0 224C60 240 125 262 177 262C240 262 300 236 354 222V240C300 256 240 287 177 287C120 287 60 262 0 246Z" fill="url(#bandA)"/>
    <path d="M0 246C60 262 120 287 177 287C240 287 300 256 354 240V290H0Z" fill="#fff"/>
  </svg>
  <div class="brand"><span class="brand__dot"></span>Velora</div>

  <article class="hotel hotel--sorrento">
    <h2 class="hotel__stay">SORRENTO – 4 NIGHTS</h2>
    <h3 class="hotel__name">HOTEL BORGO ALTO</h3>
    <div class="hotel__room">COMFORT ROOM</div>
    <div class="hotel__text">
      <p>Hotel Borgo Alto is near Piazza Tasso in the heart of Sorrento, featuring a citrus garden with a swimming pool.</p>
      <p>The helpful staff at Borgo Alto welcome you as family. They are always there to help. Pick up maps of the area, public transport schedules, and tourist information at reception.</p>
      <p>A generous American buffet breakfast is included in your room rate. Free Wi-Fi is available throughout the hotel, while the rooms also have free wired internet access. Around the pool you will find free sun loungers, umbrellas and beach towels. There is both an American bar and a poolside bar.</p>
    </div>
    <div class="hotel__link">www.hotelborgoalto.com</div>
  </article>

  <article class="hotel hotel--roma">
    <h2 class="hotel__stay">ROMA – 4 NIGHTS</h2>
    <h3 class="hotel__name">HOTEL SERENA</h3>
    <div class="hotel__room">SUPERIOR ROOM</div>
    <div class="hotel__text">
      <p>Hotel Serena is a 4 star luxury hotel located in the center of Rome, close to Campo de’ Fiori, Piazza Navona, Largo Argentina and Trastevere. This hotel is located in the building of an ancient hostel built on the remains of the walls of the Theatre of Pompeius, in Via delle Rose 12.</p>
    </div>
    <div class="hotel__link">www.hotelserenaroma.com</div>
  </article>
  <div class="page__footer"></div>
</section>

<!-- Offer page -->
<section class="page page--offer">
  <svg class="page__header" viewBox="0 0 354 290">
    <defs>
      <linearGradient id="venice" x1="0" y1="0" x2="0" y2="1">
        <stop offset="0" stop-color="#6fb0e0"/>
        <stop offset=".4" stop-color="#c9a27a"/>
        <stop offset=".65" stop-color="#3f8fb0"/>
        <stop offset="1" stop-color="#2a7a9c"/>
      </linearGradient>
      <linearGradient id="bandB" x1="0" y1="0" x2="1" y2="0">
        <stop offset="0" stop-color="var(--orange-light)"/><stop offset=".5" stop-color="var(--orange)"/><stop offset="1" stop-color="var(--orange-light)"/>
      </linearGradient>
    </defs>
    <rect role="img" aria-label="Photo: Venice Grand Canal with domed basilica and gondolas" width="354" height="290" fill="url(#venice)"/>
    <path d="M0 0H190C150 22 95 66 0 76Z" fill="#fff"/>
    <path d="M0 180C70 192 140 207 177 207C214 207 284 184 354 168V182C284 198 214 225 177 225C140 225 70 202 0 186Z" fill="url(#bandB)"/>
    <path d="M0 186C70 202 140 225 177 225C214 225 284 198 354 182V290H0Z" fill="#fff"/>
  </svg>
  <div class="brand"><span class="brand__dot"></span>Velora</div>

  <div class="promise">
    <svg class="promise__badge" viewBox="0 0 48 48" aria-hidden="true">
      <circle cx="24" cy="24" r="23" fill="var(--green)"/>
      <circle cx="24" cy="24" r="17" fill="none" stroke="#fff" stroke-width="2"/>
      <path d="M15 24l6 7 13-15" fill="none" stroke="#fff" stroke-width="4" stroke-linecap="round" stroke-linejoin="round"/>
    </svg>
    <div class="promise__list">
      <p>We guarantee top quality of all the services included.</p>
      <p>We guarantee full time assistance during your travel in Italy.</p>
      <p>We will be happy to give you complimentary contacts of our selection of favorite local restaurants and book them for you if you wish.</p>
    </div>
  </div>

  <div class="price price--person"><span class="price__label">TOUR PRICE* PER PERSON</span><span class="price__value">€ 8.115,00</span></div>
  <div class="price price--couple"><span class="price__label">TOTAL PRICE* PER COUPLE</span><span class="price__value">€ 16.230,00</span></div>

  <div class="terms terms--conditions">
    <h4 class="terms__title">CONDITIONS</h4>
    <div class="terms__rule"></div>
    <div class="terms__text">Prices are inclusive of all services mentioned in the program under “services Included”. Prices are inclusive of VAT taxes and administration fees &amp; credit card fees. All services and hotels are subject to confirmation. Payment conditions: we require 15% Non Refundable Deposit to secure your booking and the balance 60 days before departure.</div>
  </div>
  <div class="terms terms--cancel">
    <h4 class="terms__title">CANCELLATION POLICY</h4>
    <div class="terms__rule"></div>
    <div class="terms__text">
      <p>In case of cancellation of a confirmed tour, the following fees will be applied.</p>
      <p>From the day following the booking up until 60 days prior to departure: <strong>deposit (15% of tour price)</strong></p>
      <p>Between 59 and 30 days prior to departure: <strong>60% of tour price</strong></p>
      <p>From 29 days prior to departure to the date of departure, or failing to arrive at the point of departure of the Tour: <strong>100% of tour price.</strong></p>
      <p>Same cancellation policy will apply for change/cancellation of single services from the Tour package</p>
    </div>
  </div>
  <div class="page__footer">
    <span>THIS OFFER IS VALID UNTIL: <em>NOVEMBER 27TH 2019</em></span>
    <span>AND PENDING SELECTED HOTELS’ AVAILABILITY CONFIRMATION.</span>
  </div>
</section>

<!-- Packing page -->
<section class="page page--packing">
  <svg class="page__header" viewBox="0 0 354 290">
    <defs>
      <linearGradient id="sunset" x1="0" y1="0" x2="0" y2="1">
        <stop offset="0" stop-color="#d98a55"/>
        <stop offset=".45" stop-color="#e7a25a"/>
        <stop offset=".75" stop-color="#7a4a36"/>
        <stop offset="1" stop-color="#3b2a26"/>
      </linearGradient>
      <linearGradient id="bandC" x1="0" y1="0" x2="1" y2="0">
        <stop offset="0" stop-color="var(--orange-light)"/><stop offset=".5" stop-color="var(--orange)"/><stop offset="1" stop-color="var(--orange-light)"/>
      </linearGradient>
    </defs>
    <rect role="img" aria-label="Photo: Venice canal at sunset with a red ribbon heart" width="354" height="290" fill="url(#sunset)"/>
    <path d="M0 0H190C150 22 95 66 0 76Z" fill="#fff"/>
    <path d="M0 166C70 182 140 207 177 207C214 207 284 182 354 166V182C284 198 214 224 177 224C140 224 70 198 0 182Z" fill="url(#bandC)"/>
    <path d="M0 182C70 198 140 224 177 224C214 224 284 198 354 182V290H0Z" fill="#fff"/>
  </svg>
  <div class="brand"><span class="brand__dot"></span>Velora</div>

  <div class="pack" style="left:23px;top:247px"><h4 class="pack__title">ESSENTIALS</h4><ul class="pack__list">
    <li class="pack__item">Sed ut perspiciatis unde</li><li class="pack__item">omnis iste natus error</li><li class="pack__item">sit voluptatem accusantium</li><li class="pack__item">doloremque laudantium</li><li class="pack__item">totam rem aperiam, eaque</li><li class="pack__item">ipsa quae ab illo inventore</li></ul></div>
  <div class="pack" style="left:138px;top:247px"><h4 class="pack__title">PERSONAL COMFORT</h4><ul class="pack__list">
    <li class="pack__item">Sed ut perspiciatis unde</li><li class="pack__item">omnis iste natus error</li><li class="pack__item">sit voluptatem accusantium</li><li class="pack__item">doloremque laudantium</li><li class="pack__item">totam rem aperiam, eaque</li><li class="pack__item">ipsa quae ab illo inventore</li></ul></div>
  <div class="pack" style="left:252px;top:247px"><h4 class="pack__title">ELECTRONICS</h4><ul class="pack__list">
    <li class="pack__item">Sed ut perspiciatis unde</li><li class="pack__item">omnis iste natus error</li><li class="pack__item">sit voluptatem accusantium</li><li class="pack__item">doloremque laudantium</li><li class="pack__item">totam rem aperiam, eaque</li><li class="pack__item">ipsa quae ab illo inventore</li></ul></div>

  <div class="pack" style="left:23px;top:356px"><h4 class="pack__title">TOILETRIES</h4><ul class="pack__list">
    <li class="pack__item">Sed ut perspiciatis unde</li><li class="pack__item">omnis iste natus error</li><li class="pack__item">sit voluptatem accusantium</li><li class="pack__item">doloremque laudantium</li></ul></div>
  <div class="pack" style="left:138px;top:356px"><h4 class="pack__title">HEALTH &amp; BEAUTY</h4><ul class="pack__list">
    <li class="pack__item">Sed ut perspiciatis unde</li><li class="pack__item">omnis iste natus error</li><li class="pack__item">sit voluptatem accusantium</li><li class="pack__item">doloremque laudantium</li><li class="pack__item">totam rem aperiam, eaque</li></ul></div>
  <div class="pack" style="left:252px;top:356px"><h4 class="pack__title">ACCESSORIES</h4><ul class="pack__list">
    <li class="pack__item">Sed ut perspiciatis unde</li><li class="pack__item">omnis iste natus error</li><li class="pack__item">sit voluptatem accusantium</li><li class="pack__item">doloremque laudantium</li><li class="pack__item">totam rem aperiam, eaque</li><li class="pack__item">ipsa quae ab illo inventore</li></ul></div>

  <div class="pack" style="left:23px;top:432px"><h4 class="pack__title">CLOTHING</h4><ul class="pack__list">
    <li class="pack__item">Sed ut perspiciatis unde</li><li class="pack__item">omnis iste natus error</li><li class="pack__item">sit voluptatem</li></ul></div>
  <div class="pack" style="left:138px;top:439px"><h4 class="pack__title">SHOES</h4><ul class="pack__list">
    <li class="pack__item">Sed ut perspiciatis unde</li><li class="pack__item">omnis iste natus error</li><li class="pack__item">sit voluptatem</li></ul></div>
  <div class="page__footer"></div>
</section>

</body>
</html>
```